Summer Dance Program Flyer

I am the Creative Director of the Dance Ministry at our church. We are having a summer dance program that is free and open to the community. I would like a graphic design (flyer) I could use to promote the event on social media (facebook, twitter, and instagram). The flyer would need to be two-sided. (1) One side will have the Program Name: KAL Ministry Summer Dance Program; Dates: June 19, 2018 - July 21, 2018; Location: Cedar Gate Church, 5183 Palmetto Street, Temple Hills, MD 20748 - at the dance studio on the 2nd floor; Contact: Contact (301) 482-7609 or [login to view URL]@[login to view URL] for more information; as well as the following info and details: Free, Dancer image(s), captivating design. More information at [login to view URL] Please keep in mind that this is a church event, so the dancers on the flyer should not be wearing clothing that is overly revealing and ideally dancing in an uplifting way, arms up, leaps, etc. (2) The second side will have the Class Schedule attached and should include all class information listed under header.

```html
<!DOCTYPE html>
<html lang="en">
<head>
<meta charset="utf-8">
<title>KAL Ministry Summer Dance Program</title>
<link rel="stylesheet" href="https://fonts.googleapis.com/css2?family=Lobster&family=Lato:wght@300;400&family=Open+Sans:wght@400;700&display=swap">
<style>
  :root {
    --stage: #8f8f8f;
    --paper: #ffffff;
    --pink: #f7e3ef;
    --mint: #d6f1ec;
    --teal: #cdeae9;
    --lemon: #f4f3c8;
    --lilac: #e6dcef;
    --ink: #3b3b3b;
    --mauve: #7b6e7b;
    --muted: #8c8c8c;
    --rule: #a9a9a9;
    --dress: #d3c7ec;
    --skin: #efd4ad;
  }
  * { box-sizing: border-box; margin: 0; padding: 0; }
  html, body { width: 1200px; height: 877px; overflow: hidden; background: var(--stage); }
  .canvas { position: relative; width: 1200px; height: 877px; }
  .page { position: absolute; top: 20px; height: 809px; background: var(--paper); overflow: hidden; }
  .page--front { left: 16px; width: 583px; }
  .page--schedule { left: 607px; width: 582px; }
  .page svg.backdrop { position: absolute; inset: 0; }
  .page p, .page h1, .page h2, .page h3 { position: absolute; white-space: nowrap; }

  /* Front side */
  .dancer-art { position: absolute; left: 302px; top: 195px; width: 268px; height: 495px; }
  .ministry { left: 51px; top: 26px; font: 400 24px/1 "Lato", sans-serif; letter-spacing: 2px; color: var(--ink); }
  .program-title { left: 13px; top: 60px; font: 400 55px/1.1 "Lobster", cursive; color: var(--ink); }
  .dates { left: 20px; top: 157px; font: 300 21.5px/1 "Lato", sans-serif; color: var(--mauve); }
  .at-line { position: absolute; left: 44px; top: 199px; width: 260px; height: 20px; }
  .at-line::before, .at-line::after { content: ""; position: absolute; top: 10px; width: 95px; border-top: 1px solid var(--mauve); }
  .at-line::before { left: 0; } .at-line::after { right: 0; }
  .at-line span { position: absolute; left: 0; right: 0; text-align: center; font: 400 18px/20px "Lato", sans-serif; color: var(--mauve); }
  .venue { left: 20px; top: 222px; font: 300 31px/1 "Lato", sans-serif; color: var(--mauve); }
  .address { left: 20px; top: 268px; font: 400 15.5px/21.5px "Lato", sans-serif; color: var(--mauve); }
  .address .indent { padding-left: 22px; }
  .admission { left: 20px; top: 357px; width: 198px; padding: 8px 0; border-top: 1px solid var(--mauve); border-bottom: 1px solid var(--mauve); font: 400 21px/1 "Lato", sans-serif; color: var(--mauve); }
  .contact-title { left: 27px; top: 580px; font: 400 29px/1.2 "Lobster", cursive; color: var(--ink); }
  .contact-details { left: 27px; top: 621px; font: 400 18px/27px "Lato", sans-serif; color: var(--mauve); }
  .contact-details .note { font-size: 16.5px; letter-spacing: .3px; }
  .learn-title { right: 63px; top: 710px; font: 400 29px/1.2 "Lobster", cursive; color: var(--ink); }
  .links { right: 16px; top: 754px; text-align: right; font: 400 18px/24px "Lato", sans-serif; color: var(--mauve); }

  /* Schedule side */
  .schedule-title { left: 0; width: 582px; top: 36px; text-align: center; font: 400 40px/1.2 "Lobster", cursive; color: var(--ink); }
  .schedule-dates { left: 0; width: 582px; top: 84px; text-align: center; font: 400 12.5px/1 "Open Sans", sans-serif; color: var(--muted); }
  .course { position: absolute; font-family: "Open Sans", sans-serif; }
  .course--left { left: 27px; text-align: left; }
  .course--right { right: 34px; text-align: right; }
  .course h2, .course p { position: static; }
  .course-name { font: 700 18.5px/27px "Open Sans", sans-serif; color: var(--ink); letter-spacing: .3px; }
  .course-times { margin-top: 6px; font: 400 15.5px/1.4 "Open Sans", sans-serif; letter-spacing: .6px; color: var(--ink); }
  .course-instructor { margin-top: 4px; font: 700 13.5px/1.4 "Open Sans", sans-serif; color: var(--ink); }
  .course-desc { margin-top: 2px; font: 400 14px/20px "Open Sans", sans-serif; color: var(--muted); }
  .divider { position: absolute; height: 0; border-top: 1.5px solid var(--rule); }
  .footer { left: 0; width: 582px; top: 775px; text-align: center; font: 400 12px/1 "Open Sans", sans-serif; color: var(--muted); }
</style>
</head>
<body>
<main class="canvas">

  <section class="page page--front">
    <svg class="backdrop" width="583" height="809" viewBox="0 0 583 809" aria-hidden="true">
      <polygon points="0,0 583,0 583,150 0,330" fill="var(--pink)"/>
      <polygon points="0,330 300,235 0,560" fill="var(--paper)"/>
      <polygon points="0,400 260,560 0,809" fill="var(--teal)"/>
      <polygon points="0,540 583,640 583,809 0,809" fill="var(--mint)"/>
      <polygon points="230,690 583,600 583,809 260,809" fill="var(--lemon)"/>
      <polygon points="400,0 583,0 583,260" fill="var(--lilac)" opacity=".6"/>
    </svg>

    <svg class="dancer-art" role="img" aria-label="Illustration of a leaping dancer in a lavender dress with arms raised" viewBox="0 0 268 495">
      <defs>
        <linearGradient id="dancerTone" x1="0" y1="0" x2="0" y2="1">
          <stop offset="0" stop-color="var(--skin)"/>
          <stop offset=".5" stop-color="var(--dress)"/>
          <stop offset="1" stop-color="var(--skin)"/>
        </linearGradient>
      </defs>
      <rect x="0" y="0" width="268" height="495" rx="20" fill="url(#dancerTone)"/>
    </svg>

    <p class="ministry">KAL MINISTRY</p>
    <h1 class="program-title">Summer Dance Program</h1>
    <p class="dates">JUNE 19, 2018 - JULY 21, 2018</p>
    <div class="at-line"><span>at</span></div>
    <p class="venue">Cedar Gate Church</p>
    <p class="address">5183 PALMETTO STREET,<br>TEMPLE HILLS, MD 20748<br>at the dance studio on<br><span class="indent">the 2nd floor</span></p>
    <p class="admission">FREE ADMISSION</p>

    <h2 class="contact-title">Contact</h2>
    <p class="contact-details">(301) 482-7609<br>mara.vantreese@kalmail.org<br><span class="note">FOR MORE INFORMATION</span></p>
    <h2 class="learn-title">Learn More</h2>
    <p class="links">thekalministry.blog<br>cedargateonline.org/kalsummer2018</p>
  </section>

  <section class="page page--schedule">
    <svg class="backdrop" width="582" height="809" viewBox="0 0 582 809" aria-hidden="true">
      <polygon points="0,0 582,0 582,60 0,250" fill="var(--mint)"/>
      <polygon points="430,0 582,0 582,190" fill="var(--teal)" opacity=".7"/>
      <polygon points="582,330 582,620 390,809 340,809" fill="var(--pink)"/>
      <polygon points="582,560 582,809 300,809" fill="var(--lemon)"/>
    </svg>

    <h1 class="schedule-title">Class Schedule</h1>
    <p class="schedule-dates">JUNE 19, 2018 - JULY 21, 2018</p>

    <article class="course course--left" style="top:140px">
      <h2 class="course-name">MODERN TECHNIQUE AND ALIGNMENT<br>(7 and Up, All Levels)</h2>
      <p class="course-times">Tuesdays from 7pm – 8pm and Saturdays 11:30am – 1pm</p>
      <p class="course-instructor">Instructor: Mara Vantreese</p>
      <p class="course-desc">Dancers will study beginning/intermediate modern dance techniques,<br>including dynamic alignment, increased vocabulary and musicality, with<br>focus on artistry and spirituality through contemporary aesthetic.</p>
    </article>

    <div class="divider" style="left:130px; width:420px; top:339px"></div>

    <article class="course course--right" style="top:358px">
      <h2 class="course-name">DANCE AND CHOREOGRAPHY INTENSIVE<br>(Adult Only)</h2>
      <p class="course-times">Thursdays 7pm – 9pm, and Saturdays 10am – 11:30am</p>
      <p class="course-instructor">Instructor: Dana Holloway</p>
      <p class="course-desc">Dancers will learn basic dance technique and learn a dance that will be<br>ministered a the All Worship Service on Sunday, July 22, 2018 at 10am.</p>
    </article>

    <div class="divider" style="left:26px; width:374px; top:545px"></div>

    <article class="course course--left" style="top:559px">
      <h2 class="course-name">LITURGICAL CARDIO DANCE<br>(7 and Up, All Levels)</h2>
      <p class="course-times">Tuesdays from 8pm – 9pm</p>
      <p class="course-instructor">Instructor: Mara Vantreese</p>
      <p class="course-desc">This is a rigorous interval training class with high-intensity exercises.<br>The routines feature aerobic/fitness interval training with a combination<br>of fast and slow dance moves that tone and sculpt the body.</p>
    </article>

    <p class="footer">KAL MINISTRY SUMMER DANCE PROGRAM</p>
  </section>

</main>
</body>
</html>
```